Red Sea Boat trips in need of Business Card for Private Boat Tours

We need a Business card for a new business set-up in Egypt on the Red Sea for private snorkelling and boat excursions to one of the world's most beautiful reefs. We have wording logo already set-up which matches the boat but we need business cards to be bright and colourful with pictures of boat

Industry/Entity Type

Tourism

Contact Information for Business Card

Two Silver Herons (font provided) Boat Trips

```html
<!DOCTYPE html>
<html lang="en">
<head>
<meta charset="utf-8">
<title>Two Silver Herons – Business Card</title>
<link rel="stylesheet" href="https://fonts.googleapis.com/css2?family=Poppins:wght@400;500;600;700&display=swap">
<style>
  :root {
    --page-bg: #a9a9ab;
    --front-dark: #0d0f12;
    --front-coral: #3a3a36;
    --front-fish: #d8c21c;
    --back-light: #f4f6f8;
    --back-aqua: #cfe6ea;
    --ink: #111111;
    --ink-soft: #222222;
    --white: #ffffff;
    --sea-blue: #1f3fa8;
    --sea-deep: #16307f;
    --sea-teal: #1f8c9c;
    --boat-white: #dfe4ea;
  }
  * { box-sizing: border-box; margin: 0; padding: 0; }
  html, body {
    width: 1200px; height: 900px; overflow: hidden;
    background: var(--page-bg);
    font-family: "Poppins", sans-serif;
  }
  .canvas {
    position: relative; width: 1200px; height: 900px;
    display: flex; flex-direction: column; align-items: center; justify-content: center; gap: 36px;
  }
  .card {
    position: relative; width: 700px; height: 400px;
    border-radius: 26px; overflow: hidden;
    box-shadow: 0 10px 24px rgba(0,0,0,0.35);
  }
  /* Front */
  .card-front { background: var(--front-dark); }
  .front-photo {
    position: absolute; inset: 0;
    background:
      radial-gradient(ellipse 120px 80px at 38% 42%, var(--front-fish) 0%, rgba(216,194,28,0.6) 45%, transparent 75%),
      radial-gradient(ellipse 70% 55% at 55% 35%, var(--front-coral) 0%, transparent 70%),
      radial-gradient(ellipse 50% 40% at 20% 75%, #2c2c2a 0%, transparent 70%),
      var(--front-dark);
  }
  .front-wordmark {
    position: absolute; right: 44px; bottom: 46px;
    color: var(--white); font-weight: 700; font-size: 46px; letter-spacing: 0.5px;
  }
  /* Back */
  .card-back { background: var(--back-light); }
  .back-photo {
    position: absolute; inset: 0;
    background: linear-gradient(160deg, var(--back-light) 0%, #e6eff2 40%, var(--back-aqua) 75%, #b9d7dc 100%);
  }
  .back-wordmark {
    position: absolute; left: 40px; top: 150px;
    color: var(--ink); font-weight: 700; font-size: 42px;
  }
  .contact-block { position: absolute; left: 44px; top: 226px; color: var(--ink); }
  .person-name { font-weight: 600; font-size: 24px; letter-spacing: 0.5px; line-height: 1.1; }
  .person-role { font-weight: 400; font-size: 16px; color: var(--ink-soft); margin-bottom: 12px; }
  .address { font-weight: 400; font-size: 16px; line-height: 1.3; margin-bottom: 10px; }
  .contact-line { display: flex; align-items: center; gap: 8px; }
  .contact-line svg { flex: none; }
  .phone { font-weight: 600; font-size: 26px; line-height: 1.2; }
  .website { font-weight: 400; font-size: 17px; }
  .photo-cluster { position: absolute; right: 0; top: 0; }
</style>
</head>
<body>
<main class="canvas">

  <section class="card card-front" aria-label="Business card front">
    <div class="front-photo" role="img" aria-label="Photo of a yellow clownfish swimming over a dark coral reef"></div>
    <div class="front-wordmark">Two Silver Herons</div>
  </section>

  <section class="card card-back" aria-label="Business card back">
    <div class="back-photo" role="img" aria-label="Faint underwater reef photo fading to white"></div>

    <svg class="photo-cluster" width="320" height="320" viewBox="0 0 320 320" aria-hidden="false">
      <defs>
        <linearGradient id="diverTone" x1="0" y1="0" x2="0" y2="1">
          <stop offset="0" stop-color="#2a55c9"/>
          <stop offset="1" stop-color="var(--sea-deep)"/>
        </linearGradient>
        <linearGradient id="boatTone" x1="0" y1="0" x2="1" y2="1">
          <stop offset="0" stop-color="#2fa4b4"/>
          <stop offset="0.55" stop-color="var(--boat-white)"/>
          <stop offset="1" stop-color="#1b7482"/>
        </linearGradient>
        <linearGradient id="marinaTone" x1="0" y1="0" x2="1" y2="1">
          <stop offset="0" stop-color="#b98a7a"/>
          <stop offset="0.45" stop-color="var(--boat-white)"/>
          <stop offset="1" stop-color="var(--sea-teal)"/>
        </linearGradient>
      </defs>
      <g stroke-linejoin="round" stroke-width="18">
        <polygon role="img" aria-label="Photo of a snorkeller swimming above the reef"
          points="110,10 250,10 290,60 250,115 110,115 70,60" fill="url(#diverTone)" stroke="url(#diverTone)"/>
        <polygon role="img" aria-label="Photo of the tour boat deck moored in turquoise water"
          points="40,140 170,140 205,205 170,270 40,270 5,205" fill="url(#boatTone)" stroke="url(#boatTone)"/>
        <polygon role="img" aria-label="Photo of the tour boat at the marina"
          points="235,150 305,150 330,215 305,280 235,280 215,215" fill="url(#marinaTone)" stroke="url(#marinaTone)"/>
      </g>
    </svg>

    <div class="back-wordmark">Two Silver Herons</div>

    <div class="contact-block">
      <p class="person-name">KARIM ADEL</p>
      <p class="person-role">Managing Director</p>
      <p class="address">421, Address line here<br>Country Name, 45452</p>
      <p class="contact-line phone">
        <svg width="24" height="24" viewBox="0 0 24 24" aria-hidden="true">
          <circle cx="12" cy="12" r="12" fill="var(--ink)"/>
          <path d="M8.5 6.5l2 2.2-1.2 1.4c.7 1.5 1.9 2.7 3.4 3.4l1.4-1.2 2.2 2-1.1 2c-3.9-.4-8.3-4.8-8.7-8.7z" fill="var(--white)"/>
        </svg>
        044-123 456 789
      </p>
      <p class="contact-line website">
        <svg width="24" height="24" viewBox="0 0 24 24" aria-hidden="true">
          <circle cx="12" cy="12" r="12" fill="var(--ink)"/>
          <g fill="none" stroke="var(--white)" stroke-width="1.3">
            <circle cx="12" cy="12" r="6.5"/>
            <ellipse cx="12" cy="12" rx="3" ry="6.5"/>
            <line x1="5.5" y1="12" x2="18.5" y2="12"/>
          </g>
        </svg>
        www.websitename.com
      </p>
    </div>
  </section>

</main>
</body>
</html>
```